Brimble Diecast Torvel Collectables Website

looking for a vibrant web site marketplace built for diecast car enthusiasts to buy, sell, and trade with ease. Whether you're looking to showcase your own collection or discover rare and exciting models, our site makes the process simple and enjoyable. Clients can browse a curated inventory of high‑quality diecast cars, connect with fellow collectors, and find the perfect pieces to expand their collection. With a smooth user experience and a community-driven spirit, we’re the go‑to destination for anyone passionate about diecast cars.

Target Market(s)

diecast collectors

Industry/Entity Type

Diecast Collectables

Coding

Coded - Design and coding required

Number of Pages Required

3 page

Font styles to use
Sans Serif

Colors
EE7325
F08F49
F5BC92
FAE3D3
FDF4ED

Requirements
Must have
• Cool look and feel. Woo commerce page to post and sell my inventory
Nice to have
• page for users to post their cars or looking for trades.
Should not have
• look cheap

```html
<!DOCTYPE html>
<html lang="en">
<head>
<meta charset="utf-8">
<title>Brimble Diecast – Torvel Collectables</title>
<link href="https://fonts.googleapis.com/css2?family=Cinzel:wght@500;600;700&family=Poppins:wght@400;500;600&family=Nunito+Sans:wght@400;600&family=Arimo:wght@400;600&display=swap" rel="stylesheet">
<style>
:root{
  --orange:#EE7325;
  --orange-soft:#F08F49;
  --peach:#F5BC92;
  --cream:#FAE3D3;
  --ivory:#FDF4ED;
  --brown:#2a1f17;
  --dark:#2b2420;
  --maroon:#5a3440;
  --tan:#d6a05e;
  --ink:#1e1e1e;
  --grey:#6b6b6b;
}
*{margin:0;padding:0;box-sizing:border-box}
html,body{width:1200px;height:3147px;overflow:hidden}
body{position:relative;background:#fff;font-family:"Nunito Sans",sans-serif;color:var(--ink)}
.abs{position:absolute}

.top-bar{left:0;top:0;width:1200px;height:43px;background:var(--brown);color:#fff;font-family:"Poppins",sans-serif;font-size:15px;font-weight:500}
.top-bar .call{left:112px;top:12px;display:flex;align-items:center;gap:10px}
.top-bar .call span{font-weight:400}
.top-bar .login{left:802px;top:10px;display:flex;gap:8px;align-items:center}
.top-bar .support{left:918px;top:10px;display:flex;gap:8px;align-items:center}

.main-nav{left:0;top:43px;width:1200px;height:85px;background:#fff;font-family:"Cinzel",serif;font-size:17px;font-weight:600;color:var(--brown)}
.main-nav a{position:absolute;top:38px;color:inherit;text-decoration:none;letter-spacing:.5px}
.main-nav a.active{color:var(--orange);font-size:21px;top:35px}
.brand{left:505px;top:10px;width:190px;height:118px;display:flex;flex-direction:column;align-items:center;justify-content:center;gap:8px;background:#fff;border-radius:0 0 30px 30px;z-index:3}
.brand .dot{width:34px;height:34px;border-radius:50%;background:var(--orange)}
.brand .name{font-family:"Cinzel",serif;font-weight:700;font-size:19px;color:var(--brown);text-align:center;line-height:1.1}

.hero{left:0;top:128px;width:1200px;height:624px;background:radial-gradient(ellipse at 30% 25%,#5a4a3a 0%,transparent 45%),radial-gradient(ellipse at 82% 65%,#8a1c1c 0%,transparent 30%),linear-gradient(180deg,#2f2a26 0%,#1e1a17 55%,#3a342f 100%)}
.hero-text{left:94px;top:282px;color:#fff;font-family:"Cinzel",serif;font-weight:700}
.hero-text .kicker{font-size:31px;letter-spacing:1px}
.hero-text h1{font-size:52px;line-height:55px;margin-top:6px;letter-spacing:1px}
.btn-shop{left:94px;top:450px;width:153px;height:51px;background:var(--orange);color:#fff;font-family:"Cinzel",serif;font-weight:700;font-size:19px;display:flex;align-items:center;justify-content:center;letter-spacing:1px;border-radius:2px}

.section-title{left:0;width:1200px;text-align:center;font-family:"Cinzel",serif;font-weight:600;font-size:41px;color:var(--brown);letter-spacing:1px}
.title-rule{left:567px;width:66px;height:3px;background:var(--orange)}

.shop-card{top:932px;width:313px;height:357px;background:#fff;box-shadow:0 0 10px rgba(0,0,0,.12);border-radius:4px}
.shop-card .car{position:absolute;left:25px;top:21px;width:263px;height:135px;border-radius:60px 60px 20px 20px}
.shop-card h3{position:absolute;left:0;top:174px;width:100%;text-align:center;font-family:"Cinzel",serif;font-weight:600;font-size:21px;color:var(--brown)}
.spec{position:absolute;left:27px;top:213px;width:266px;border-collapse:collapse;background:#ececec;font-family:"Arimo",sans-serif;font-size:17px;color:#333}
.spec td{height:57px;text-align:center;border:2px solid #fff;width:50%}
.arrow-btn{top:1093px;width:34px;height:34px}

.services{left:0;top:1381px;width:1200px;height:458px;background:radial-gradient(ellipse at 70% 20%,#3a302a 0%,transparent 50%),var(--dark)}
.service{top:1473px;width:320px;text-align:center;color:#fff}
.service .icon{width:100px;height:100px;border-radius:50%;margin:0 auto;display:flex;align-items:center;justify-content:center}
.service h3{font-family:"Cinzel",serif;font-weight:700;font-size:26px;margin-top:21px;letter-spacing:1px}
.service p{font-size:16.5px;line-height:26px;margin-top:12px}

.blog-main{left:138px;top:2019px;width:445px;height:452px;background:#fff;box-shadow:0 0 10px rgba(0,0,0,.1)}
.blog-main .photo{position:absolute;left:8px;top:9px;width:430px;height:291px;background:linear-gradient(135deg,#6d5848,#b9a590 55%,#8a7f76)}
.blog-main h4{position:absolute;top:326px;width:100%;text-align:center;font-family:"Arimo",sans-serif;font-weight:600;font-size:16.5px}
.blog-main .meta{top:354px;width:100%;justify-content:center}
.blog-main p{position:absolute;top:381px;left:40px;width:365px;text-align:center;font-family:"Arimo",sans-serif;font-size:14px;line-height:22px;color:var(--grey)}
.meta{position:absolute;display:flex;gap:6px;align-items:center;font-family:"Arimo",sans-serif;font-size:13.5px;color:var(--orange)}
.meta .sep{color:var(--grey);margin:0 4px}
.blog-side{left:617px;width:445px;height:138px;background:#fff;box-shadow:0 0 10px rgba(0,0,0,.1)}
.blog-side .photo{position:absolute;left:9px;top:9px;width:152px;height:120px;background:linear-gradient(135deg,#7a6a5e,#c9bdb1 60%,#5e6a74)}
.blog-side h4{position:absolute;left:179px;top:18px;font-family:"Arimo",sans-serif;font-weight:400;font-size:15.5px;color:#222}
.blog-side .meta{left:179px;top:43px}
.blog-side p{position:absolute;left:179px;top:71px;width:240px;font-family:"Arimo",sans-serif;font-size:14px;line-height:20px;color:var(--grey)}

.footer{left:0;top:2670px;width:1200px;height:477px;background:#000}
.footer-col{top:2752px;color:#fff;font-family:"Poppins",sans-serif}
.footer-col h5{font-size:22px;font-weight:600;margin-bottom:10px}
.footer-col ul{list-style:none;font-size:15px}
.footer-col li{height:31px;display:flex;align-items:center;gap:10px}
.contact-item{display:flex;align-items:center;gap:11px;font-size:15px;height:60px}
.contact-item .ci{width:38px;height:38px;border-radius:50%;background:var(--orange);display:flex;align-items:center;justify-content:center}
.news p{font-size:15px;line-height:31px;margin-top:4px}
.news .field{margin-top:8px;width:269px;border-bottom:2px solid #fff;padding:0 0 10px 3px;font-size:15px}
.news .subscribe{margin-top:30px;width:145px;height:49px;border-radius:25px;background:var(--orange);display:flex;align-items:center;justify-content:center;font-size:17px;font-weight:500}
.footer-rule{left:95px;top:3057px;width:1004px;height:1px;background:#777}
.copyright{left:0;top:3088px;width:1200px;text-align:center;color:#fff;font-family:"Poppins",sans-serif;font-weight:600;font-size:16px}
</style>
</head>
<body>

<header class="abs top-bar">
  <div class="abs call">
    <svg width="14" height="14" viewBox="0 0 24 24"><path fill="#fff" d="M6.6 10.8a15 15 0 006.6 6.6l2.2-2.2a1 1 0 011-.25 11 11 0 003.6.6 1 1 0 011 1V20a1 1 0 01-1 1A17 17 0 013 4a1 1 0 011-1h3.5a1 1 0 011 1 11 11 0 00.6 3.6 1 1 0 01-.25 1z"/></svg>
    Call Us Now: <span>+1888 888 8888</span>
  </div>
  <div class="abs login">
    <svg width="12" height="14" viewBox="0 0 12 14"><circle cx="6" cy="4" r="3.3" fill="#fff"/><path d="M0 14a6 6 0 0112 0z" fill="#fff"/></svg>Log In
  </div>
  <div class="abs support">
    <svg width="16" height="14" viewBox="0 0 16 14"><path d="M2 8a6 6 0 0112 0" stroke="#fff" stroke-width="2" fill="none"/><rect x="1" y="7" width="3" height="5" rx="1" fill="#fff"/><rect x="12" y="7" width="3" height="5" rx="1" fill="#fff"/></svg>Customer Support
  </div>
</header>

<nav class="abs main-nav">
  <a class="active" style="left:112px">Home</a>
  <a style="left:218px">Shop</a>
  <a style="left:307px">Sell</a>
  <a style="left:387px">Buy</a>
  <a style="left:729px">About</a>
  <a style="left:827px">Community</a>
  <a style="left:985px">Blog</a>
</nav>
<div class="abs brand"><span class="dot"></span><span class="name">Brimble<br>Diecast</span></div>

<section class="abs hero" role="img" aria-label="Night scene of a lit windmill by the water with a red classic convertible model car in the foreground"></section>
<div class="abs hero-text">
  <div class="kicker">WELCOME TO</div>
  <h1>THE ULTIMATE HUB<br>DIECAST COLLECTORS.</h1>
</div>
<div class="abs btn-shop">SHOP NOW</div>

<svg class="abs" style="left:0;top:600px" width="1200" height="160" viewBox="0 0 1200 160">
  <path d="M0 32 L180 62 Q205 66 225 82 Q245 96 270 100 L600 148 L930 100 Q955 96 975 82 Q995 66 1020 62 L1200 32 L1200 160 L0 160Z" fill="#fff"/>
  <path d="M0 22 L180 52 Q205 56 225 72 Q245 86 270 90 L600 138 L930 90 Q955 86 975 72 Q995 56 1020 52 L1200 22" stroke="#fff" stroke-width="4" fill="none"/>
  <path d="M0 32 L180 62 Q205 66 225 82 Q245 96 270 100 L600 148 L930 100 Q955 96 975 82 Q995 66 1020 62 L1200 32" stroke="var(--brown)" stroke-width="14" fill="none"/>
</svg>

<h2 class="abs section-title" style="top:834px">OUR SHOP</h2>
<div class="abs title-rule" style="top:891px"></div>

<svg class="abs arrow-btn" style="left:39px" viewBox="0 0 34 34"><circle cx="17" cy="17" r="15.5" fill="#fff" stroke="#111" stroke-width="1.5"/><path d="M19.5 11l-6 6 6 6" stroke="#111" stroke-width="1.8" fill="none"/></svg>
<svg class="abs arrow-btn" style="left:1124px" viewBox="0 0 34 34"><circle cx="17" cy="17" r="15.5" fill="#fff" stroke="#111" stroke-width="1.5"/><path d="M14.5 11l6 6-6 6" stroke="#111" stroke-width="1.8" fill="none"/></svg>

<article class="abs shop-card" style="left:111px">
  <div class="car" role="img" aria-label="Blue sports model car" style="background:radial-gradient(ellipse at 50% 55%,#2a5bd1 0%,#1b3c96 45%,#fff 72%)"></div>
  <h3>DIECAST CARS</h3>
  <table class="spec"><tr><td>BRAND</td><td>YEAR</td></tr><tr><td>BRAND</td><td>YEAR</td></tr></table>
</article>
<article class="abs shop-card" style="left:444px">
  <div class="car" role="img" aria-label="Yellow vintage model car" style="background:radial-gradient(ellipse at 50% 55%,#f2cc1c 0%,#d6a90e 42%,#fff 70%)"></div>
  <h3>DIECAST CARS</h3>
  <table class="spec"><tr><td>BRAND</td><td>YEAR</td></tr><tr><td>BRAND</td><td>YEAR</td></tr></table>
</article>
<article class="abs shop-card" style="left:776px">
  <div class="car" role="img" aria-label="Teal classic coupe model car" style="background:radial-gradient(ellipse at 50% 55%,#3cc6b8 0%,#229a90 40%,#fff 66%)"></div>
  <h3>DIECAST CARS</h3>
  <table class="spec"><tr><td>BRAND</td><td>YEAR</td></tr><tr><td>BRAND</td><td>YEAR</td></tr></table>
</article>

<section class="abs services"></section>
<div class="abs service" style="left:97px">
  <div class="icon" style="background:var(--orange)"><svg width="50" height="46" viewBox="0 0 50 46"><path d="M2 6h8l6 24h24l5-16H13" stroke="#fff" stroke-width="4" fill="none" stroke-linejoin="round"/><circle cx="19" cy="39" r="4" fill="#fff"/><circle cx="37" cy="39" r="4" fill="#fff"/><path d="M26 14l5 5 9-10" stroke="#fff" stroke-width="4" fill="none"/></svg></div>
  <h3>BUYING</h3>
  <p>Browse verified listings from collectors worldwide. Each listing includes detailed descriptions and photos so you can shop with confidence.</p>
</div>
<div class="abs service" style="left:440px">
  <div class="icon" style="background:var(--tan)"><svg width="48" height="48" viewBox="0 0 48 48"><circle cx="30" cy="14" r="11" fill="#fff"/><text x="30" y="19" font-size="14" font-family="Arial" font-weight="700" text-anchor="middle" fill="#d6a05e">$</text><rect x="4" y="28" width="8" height="16" fill="#fff"/><path d="M14 30h12l10 4 8-4v8l-14 6H14z" fill="#fff"/></svg></div>
  <h3>SELLING</h3>
  <p>urn your collection into cash. List your diecast cars in minutes with our simple selling tools and reach thousands of collectors instantly.</p>
</div>
<div class="abs service" style="left:785px">
  <div class="icon" style="background:var(--orange)"><svg width="50" height="46" viewBox="0 0 50 46"><path d="M4 18l12-10 8 6 14-11" stroke="#fff" stroke-width="4" fill="none"/><path d="M34 2h7v7" stroke="#fff" stroke-width="4" fill="none"/><rect x="4" y="26" width="8" height="18" rx="2" fill="#fff"/><rect x="15" y="20" width="8" height="24" rx="2" fill="#fff"/><rect x="26" y="24" width="8" height="20" rx="2" fill="#fff"/><rect x="37" y="16" width="8" height="28" rx="2" fill="#fff"/></svg></div>
  <h3>TRADING</h3>
  <p>Prefer to swap? Connect with other collectors and trade models securely through our built-in messaging and trade-offer system.</p>
</div>

<h2 class="abs section-title" style="top:1917px">LATEST BLOG</h2>
<div class="abs title-rule" style="top:1970px;left:559px;width:82px;background:var(--maroon)"></div>

<article class="abs blog-main">
  <div class="photo" role="img" aria-label="Three colleagues reviewing documents at a laptop in an office"></div>
  <h4>Lorem ipsum dolor sit amet, consectetur adipi</h4>
  <div class="meta"><span>&#128197; August 13, 2025</span><span class="sep">|</span><span>&#128100; Laura</span></div>
  <p>Sed ut perspiciatis unde omnis iste natus error sit voluptatem accusantium doloremque</p>
</article>

<article class="abs blog-side" style="top:2019px">
  <div class="photo" role="img" aria-label="Businesswoman holding a tablet in an office"></div>
  <h4>Lorem ipsum dolor sit amet, consec</h4>
  <div class="meta"><span>&#128197; August 13, 2025</span><span class="sep">|</span><span>&#128100; Laura</span></div>
  <p>Sed ut perspiciatis unde omnis iste natus error sit voluptatem</p>
</article>
<article class="abs blog-side" style="top:2175px">
  <div class="photo" role="img" aria-label="Business team seated together in a meeting space"></div>
  <h4>Lorem ipsum dolor sit amet, consec</h4>
  <div class="meta"><span>&#128197; August 13, 2025</span><span class="sep">|</span><span>&#128100; Laura</span></div>
  <p>Sed ut perspiciatis unde omnis iste natus error sit voluptatem</p>
</article>
<article class="abs blog-side" style="top:2332px">
  <div class="photo" role="img" aria-label="Colleagues working at a desk with a laptop"></div>
  <h4>Lorem ipsum dolor sit amet, consec</h4>
  <div class="meta"><span>&#128197; August 13, 2025</span><span class="sep">|</span><span>&#128100; Laura</span></div>
  <p>Sed ut perspiciatis unde omnis iste natus error sit voluptatem</p>
</article>

<svg class="abs" style="left:0;top:2540px" width="1200" height="140" viewBox="0 0 1200 140">
  <path d="M0 142 L200 100 Q230 94 250 80 Q270 66 300 62 L600 14 L900 62 Q930 66 950 80 Q970 94 1000 100 L1200 142 L1200 140 L0 140Z" fill="#000"/>
  <path d="M0 128 L200 86 Q230 80 250 66 Q270 52 300 48 L600 0 L900 48 Q930 52 950 66 Q970 80 1000 86 L1200 128" stroke="#fff" stroke-width="4" fill="none"/>
  <path d="M0 138 L200 96 Q230 90 250 76 Q270 62 300 58 L600 10 L900 58 Q930 62 950 76 Q970 90 1000 96 L1200 138" stroke="var(--brown)" stroke-width="14" fill="none"/>
</svg>

<footer class="abs footer"></footer>
<div class="abs footer-col" style="left:94px">
  <h5>Quick Links</h5>
  <ul>
    <li>&#10140; Home</li><li>&#10140; About Us</li><li>&#10140; Menu</li><li>&#10140; Order Online</li><li>&#10140; What’s New</li><li>&#10140; Contact Us</li>
  </ul>
</div>
<div class="abs footer-col" style="left:293px">
  <h5>Other Links</h5>
  <ul>
    <li>&#10140; FAQ</li><li>&#10140; Tems of Use</li><li>&#10140; Privacy Policy</li><li>&#10140; Support Links</li><li>&#10140; Conditions</li>
  </ul>
</div>
<div class="abs footer-col" style="left:505px">
  <h5>Contact Us</h5>
  <div class="contact-item"><span class="ci"><svg width="14" height="18" viewBox="0 0 14 18"><path d="M7 0a7 7 0 017 7c0 5-7 11-7 11S0 12 0 7a7 7 0 017-7z" fill="#fff"/><circle cx="7" cy="7" r="2.5" fill="#EE7325"/></svg></span>Company Name,United State.</div>
  <div class="contact-item"><span class="ci"><svg width="16" height="12" viewBox="0 0 16 12"><rect width="16" height="12" rx="1.5" fill="#fff"/><path d="M1 1l7 6 7-6" stroke="#EE7325" stroke-width="1.5" fill="none"/></svg></span>info@compancyname.in</div>
  <div class="contact-item"><span class="ci"><svg width="15" height="15" viewBox="0 0 24 24"><path fill="#fff" d="M6.6 10.8a15 15 0 006.6 6.6l2.2-2.2a1 1 0 011-.25 11 11 0 003.6.6 1 1 0 011 1V20a1 1 0 01-1 1A17 17 0 013 4a1 1 0 011-1h3.5a1 1 0 011 1 11 11 0 00.6 3.6 1 1 0 01-.25 1z"/></svg></span>+1888 8888 8888</div>
</div>
<div class="abs footer-col news" style="left:825px">
  <h5>Sign Up To Our Newsletter</h5>
  <p>Lorem ipsum dolor sit amet,consectetur<br>adipiscing elit,adipiscing elit.</p>
  <div class="field">Email</div>
  <div class="subscribe">Subscribe</div>
</div>
<div class="abs footer-rule"></div>
<div class="abs copyright">Copyrights@2026.Company Name.All Rights Reserved</div>

</body>
</html>
```